Industrial Consulting Firm Looking for a Responsive Design

Looking for a responsive design website of around 5 parent pages and about another 15 sub-pages for a small firm that works globally at industrial construction sites.

The web address http://torvexmilan.com/brightlo482917/index.html includes most of the content we would like to use for this effort. There are two deliverable options:

1) Use the provided design and create graphics for the website along with other requested tweaks.
2) Create a entirely new Layout/Design, which is original and different from this example, using content (text) from the provided link.

Content:

The main components of the website should include graphics for main page headers and picture links (along with the 7 main service sub pages), with industrial themes for the following pages:

Landing Page with clean presentation of our company and services.

Services: This main page has the most important sub-links in the website, the services which we want to highlight (Statistical Productivity Improvement, Veradin Process, Improving Project Performance, Work Process Analysis & Mapping, On-Site Training, and Facilitation Support). We would like to see graphic headers for each of these pages. Would like to have a fact sheet template.

News & Insight (Blog/Content Delivery format for press releases, latest news, publications, ability to be linked to company facebook feed a plus, etc)

Information about the company (Mission, Description, Company Profile, Clients Served,FAQs). Also, an interactive world map of past projects with capacity to update. It should work by obtaining a detail summary of past projects by hovering/clicking locations.

Contact Form including link to careers

Feel free to update any tables or content in pages. Ideas to highlight our services through graphics are appreciated.

Optional Features To Consider:

Client Testimonial Section (possibly on Main Page or About Us)
Filtering of News by Category/Date
Basic Site Search Functionality
Add a Registration option for Site Updates

Other Details:

If using pictures with people wearing safety gear: make sure that they are wearing safety glasses and a hard hat at a minimum and that the picture looks as realistic (environment-wise) as possible
Guidance on inclusion of other company logos in websites (as clients references, or displayed in pictures). Potentially looking to include them in website (either on landing page or clients served section in about us).

Important Considerations:

The design should be mobile (Android, IOS) friendly (NOT a separate mobile site)
The design should incorporate SEO.
The design should take security into account.
Coding required as well as graphic template files.

Upcoming Project Opportunity

Based on the demonstrated graphic design presented in this project, we might consider an additional project to expand on graphics package (including, but not limited to an info graphic).

Technical Requirements:

Languages Accepted: HTML, ASP.NET
To Run on a Server with: Windows IIS 7 or above
Restrictions: No languages requiring install on Windows IIS
Easily updated and maintained

Project will commit payment when we find at least one design our team agrees upon.

```html
<!DOCTYPE html>
<html lang="en">
<head>
<meta charset="utf-8">
<title>Veltrane Performance Group, Inc.</title>
<link rel="stylesheet" href="https://fonts.googleapis.com/css2?family=Open+Sans:wght@300;400;600;700&display=swap">
<style>
:root{
  --brown:#8c6b50;
  --brown-dark:#7a5b42;
  --ink:#3b3b3b;
  --muted:#7d7268;
  --text:#6a6a6a;
  --light:#f2f2f2;
  --line:#dcdcdc;
  --topbar:#3a3a3a;
  --footer:#2f2f2f;
  --footer-deep:#262626;
  --footer-text:#9a9a9a;
  --white:#ffffff;
}
*{margin:0;padding:0;box-sizing:border-box}
html,body{width:1200px;height:2406px;overflow:hidden}
body{position:relative;font-family:"Open Sans",Arial,sans-serif;color:var(--text);background:var(--white);font-size:12px}
.block{position:absolute;left:0;width:1200px}
.wrap{position:absolute;left:156px;width:888px}

/* top bar */
.topbar{top:0;height:59px;background:var(--topbar);border-top:4px solid var(--brown)}
.social{position:absolute;left:166px;top:24px;display:flex;gap:12px}
.social span{width:9px;height:9px;border-radius:50%;background:#cfcfcf;display:block}
.nav{position:absolute;left:557px;top:9px;display:flex;height:46px;align-items:center;font-size:13px}
.nav a{color:#e6e6e6;text-decoration:none;padding:0 16px;height:46px;line-height:46px}
.nav a.active{background:var(--white);color:var(--brown)}

/* header */
.header{top:59px;height:81px;background:var(--white)}
.brand{position:absolute;left:164px;top:16px;display:flex;align-items:center;gap:10px}
.brand-mark{width:44px;height:44px;border-radius:50%;background:var(--brown)}
.brand-name{font-size:13px;font-weight:700;color:var(--ink);line-height:15px;letter-spacing:1px;text-transform:uppercase;width:130px}
.contact-line{position:absolute;left:773px;top:10px;font-size:11px;color:#9a9a9a;display:flex;gap:14px}
.contact-line svg{vertical-align:-2px;margin-right:4px}
.search{position:absolute;left:773px;top:32px;width:266px;height:31px;border:1px solid var(--line);background:var(--white)}
.search-btn{position:absolute;right:-1px;top:-1px;width:37px;height:31px;background:var(--brown);display:flex;align-items:center;justify-content:center}

/* hero */
.hero{top:140px;height:359px;background:radial-gradient(ellipse at 52% 45%,#c7a27f 0%,#a9896c 22%,#d9d4cd 55%,#eceae6 100%)}
.hero-caption{position:absolute;left:109px;top:158px;width:478px;height:164px;background:rgba(255,255,255,.72);border-left:4px solid var(--brown);padding:18px 28px}
.hero-caption h2{font-weight:400;font-size:22px;color:var(--brown);margin-bottom:12px}
.hero-caption p{font-size:14px;line-height:21px;color:#8b8580}
.hero-arrow{position:absolute;top:162px;width:26px;height:26px;border-radius:50%;background:rgba(255,255,255,.55);display:flex;align-items:center;justify-content:center}

/* welcome */
.welcome{top:499px;height:122px;background:var(--brown);display:flex;align-items:center;justify-content:center;color:var(--white);font-size:30px;font-weight:300;letter-spacing:.5px}
.welcome strong{font-weight:700;margin-left:10px}

/* company */
.company{top:621px;height:470px;background:var(--white)}
.section-title{font-size:24px;font-weight:400;color:var(--ink);text-transform:uppercase}
.company .section-title{position:absolute;top:40px;width:100%;text-align:center}
.company-intro{position:absolute;top:78px;left:0;width:888px;text-align:center;font-size:14px;line-height:24px;color:var(--muted)}
.col-title{font-size:19px;font-weight:400;color:var(--brown);text-transform:uppercase;margin-bottom:14px}
.industries{position:absolute;left:0;top:214px;width:409px;text-align:right}
.clients{position:absolute;left:481px;top:214px;width:409px}
.col-text{font-size:11.5px;line-height:20px;color:var(--text)}
.divider{position:absolute;left:444px;top:216px;width:1px;height:254px;background:var(--line)}

/* services */
.services{top:1091px;height:459px;background:var(--light);border-top:1px solid #e4e4e4}
.services-intro{position:absolute;left:156px;top:46px;width:222px}
.title-line{font-size:24px;color:var(--ink);text-transform:uppercase;border-bottom:1px solid #cfcfcf;padding-bottom:4px;font-weight:400}
.title-line strong{font-weight:700}
.services-intro p{margin-top:16px;font-size:11.5px;line-height:19.5px;color:var(--text)}
.pager{margin-top:28px;display:flex;gap:8px}
.pager span{width:18px;height:18px;background:#cfcfcf;display:flex;align-items:center;justify-content:center}
.pager span.on{background:#9a9a9a}
.tiles{position:absolute;left:387px;top:45px;width:657px;display:grid;grid-template-columns:repeat(3,208px);grid-auto-rows:177px;gap:16px 16px}
.tile{position:relative;display:flex;flex-direction:column;align-items:center;justify-content:center;text-align:center;padding:0 10px;color:var(--white)}
.tile h3{font-size:12.5px;font-weight:600;margin-bottom:3px;text-shadow:0 1px 2px rgba(0,0,0,.4)}
.tile p{font-size:10px;line-height:14px;opacity:.9;text-shadow:0 1px 2px rgba(0,0,0,.4)}
.tile-stats{background:linear-gradient(160deg,#3d8be0,#1d52b5 70%,#173f8e)}
.tile-project{background:linear-gradient(160deg,#c99768,#a86a3a 55%,#7a4521)}
.tile-training{background:linear-gradient(160deg,#e8ecef,#9fa9b1 60%,#5d6972)}
.tile-veradin{background:linear-gradient(160deg,#a5a5a5,#757575 60%,#585858)}
.tile-mapping{background:linear-gradient(160deg,#d6dde6,#8aa6c4 50%,#4d6e99)}
.tile-facilitation{background:linear-gradient(160deg,#2c5ea8,#173f7a 55%,#0d2347)}

/* join */
.join{top:1550px;height:96px;background:var(--white)}
.join-text{position:absolute;left:156px;top:30px;font-size:21px;color:var(--brown);font-weight:400}
.join-btn{position:absolute;left:804px;top:27px;width:240px;height:40px;background:var(--brown);color:var(--white);font-size:12px;letter-spacing:.5px;display:flex;align-items:center;justify-content:center;border-radius:2px}

/* news + testimonials */
.updates{top:1646px;height:394px;background:var(--light);border-top:1px solid #e4e4e4}
.news{position:absolute;left:156px;top:42px;width:400px}
.news-item{padding:16px 0 12px;border-bottom:1px solid var(--line)}
.news-item:last-child{border-bottom:1px solid var(--line)}
.news-item h4{font-size:11.5px;font-weight:400;color:var(--brown);margin-bottom:3px}
.news-item p{font-size:11.5px;line-height:19.5px;color:var(--text)}
.testimonials{position:absolute;left:645px;top:42px;width:399px}
.quote{display:flex;gap:28px;margin-top:24px}
.quote + .quote{margin-top:30px}
.avatar{width:106px;height:105px;flex:none;background:linear-gradient(160deg,#e9e6e2,#cfc7bf);border:4px solid var(--white)}
.quote p{font-size:11.5px;line-height:19.5px;color:#555;padding-top:10px}
.quote em{color:#666}

/* footer */
.footer{top:2040px;height:281px;background:var(--footer)}
.foot-logo{position:absolute;left:156px;top:40px;width:184px;height:54px;background:var(--white);display:flex;align-items:center;gap:8px;padding:0 8px;border:2px solid #bdbdbd}
.foot-logo .brand-mark{width:34px;height:34px}
.foot-logo .brand-name{font-size:10.5px;line-height:12px;width:130px}
.foot-contact{position:absolute;left:156px;top:110px;font-size:11px;line-height:22.5px;color:var(--footer-text)}
.foot-contact svg{vertical-align:-1px;margin-right:5px}
.foot-map{position:absolute;left:156px;top:182px;width:180px;height:72px;background:radial-gradient(ellipse at center,#3a3a3a,#2f2f2f 70%)}
.foot-col{position:absolute;top:52px;width:210px}
.foot-col h5{font-size:18px;font-weight:400;color:var(--white);margin-bottom:14px}
.foot-col h5 strong{font-weight:700}
.foot-col ul{list-style:none}
.foot-col li{font-size:11px;line-height:26.5px;color:var(--footer-text)}
.foot-col li::before{content:"› ";}
.tweet{display:flex;gap:10px;font-size:11px;line-height:19px;color:var(--footer-text);padding-bottom:10px;margin-bottom:10px;border-bottom:1px solid #3d3d3d}
.tweet-dot{width:10px;height:10px;border-radius:50%;background:#8a8a8a;flex:none;margin-top:4px}
.tweet small{display:block;font-size:8.5px;color:#777;line-height:14px}

/* bottom bar */
.bottom{top:2321px;height:85px;background:var(--footer-deep)}
.notch{position:absolute;left:589px;top:0;width:0;height:0;border-left:12px solid transparent;border-right:12px solid transparent;border-top:10px solid var(--footer)}
.copyright{position:absolute;left:156px;top:36px;font-size:10px;color:#7a7a7a}
.bottom-social{position:absolute;left:855px;top:33px;display:flex;gap:8px}
.bottom-social span{width:19px;height:19px;border-radius:50%;background:#555;display:block}
</style>
</head>
<body>

<div class="block topbar">
  <div class="social"><span></span><span></span><span></span><span></span><span></span><span></span><span></span></div>
  <nav class="nav">
    <a class="active">Home</a><a>Services</a><a>News &amp; Insights</a><a>About Us</a><a>Contact</a><a>Login</a>
  </nav>
</div>

<header class="block header">
  <div class="brand"><span class="brand-mark"></span><span class="brand-name">Veltrane Performance Group</span></div>
  <div class="contact-line">
    <span><svg width="11" height="8" viewBox="0 0 11 8"><rect x="0.5" y="0.5" width="10" height="7" fill="none" stroke="#b0b0b0"/><path d="M.5 .5 5.5 4.5 10.5 .5" fill="none" stroke="#b0b0b0"/></svg>info@veltraneperf.com</span>
    <span><svg width="9" height="10" viewBox="0 0 9 10"><path d="M1 1h2l1 2.5-1.2.8a5 5 0 0 0 2.9 2.9L6.5 6 9 7v2a1 1 0 0 1-1 1A8 8 0 0 1 0 2a1 1 0 0 1 1-1z" fill="#b0b0b0"/></svg>+1 555.014.2288</span>
  </div>
  <div class="search">
    <div class="search-btn"><svg width="14" height="14" viewBox="0 0 14 14"><circle cx="6" cy="6" r="4.3" fill="none" stroke="#fff" stroke-width="1.8"/><path d="M9.2 9.2 13 13" stroke="#fff" stroke-width="2"/></svg></div>
  </div>
</header>

<section class="block hero" role="img" aria-label="Hero photograph: cupped hands holding soil with a young green seedling">
  <div class="hero-arrow" style="left:18px"><svg width="10" height="10" viewBox="0 0 10 10"><path d="M6.5 1 2.5 5l4 4" fill="none" stroke="#fff" stroke-width="1.6"/></svg></div>
  <div class="hero-arrow" style="right:18px"><svg width="10" height="10" viewBox="0 0 10 10"><path d="M3.5 1l4 4-4 4" fill="none" stroke="#fff" stroke-width="1.6"/></svg></div>
  <div class="hero-caption">
    <h2>VPG's Offers</h2>
    <p>Refined, collaborative, award-winning methodologies designed to supplement traditional performance measurements, resulting in a positive influence on safety, Quality, and client's bottom line.</p>
  </div>
</section>

<section class="block welcome">WELCOME TO <strong>VELTRANE PERFORMANCE GROUP, INC.</strong></section>

<section class="block company">
  <div class="wrap" style="top:0;height:470px">
    <h2 class="section-title">Our Company</h2>
    <p class="company-intro">Veltrane Performance Group, Inc. (VPG) is a performance improvement firm specializing in providing improvement services for the engineering and construction industry . VPG utilizes award-winning industry "Best Practice" measurement techniques, combined with proven Lean Construction and Total Quality Management concepts to drive improvement of project execution performance and ultimately help clients increase their bottom lines.</p>
    <div class="industries">
      <h3 class="col-title">Industries</h3>
      <p class="col-text">VPG has provided improvement services to many industry leading engineering and construction companies and facility owners all around the world. VPG services have been implemented successfully across a broad spectrum of industry sectors including Oil &amp; Gas, Mining, Utilities (fossil, hydro and nuclear), Chemical Products, Refinery Products, Industrial fabrication for both onshore and offshore facilities and many more.</p>
    </div>
    <div class="divider"></div>
    <div class="clients">
      <h3 class="col-title">Our Clients</h3>
      <p class="col-text">VPG has partnered with clients on their most critical projects around the world. Some of these companies include :</p>
      <p class="col-text" style="margin-top:18px">Corvane, Hallstead Energy, Edrix, Meridane Oil, Brantwell Products North America, J. Olen Marcroft, Calder Valley Power Authority, Fenwright Daniels, Jessop, Stallard, Building Trades of Northvale.</p>
    </div>
  </div>
</section>

<section class="block services">
  <div class="services-intro">
    <h2 class="title-line">Our <strong>Services</strong></h2>
    <p>VPG assumes the vast majority of the craft workforce strives to be productive and true productivity improvement will result when project management removes the BARRIERS to productivity.</p>
    <div class="pager">
      <span><svg width="8" height="8" viewBox="0 0 8 8"><path d="M5.5 1 2.5 4l3 3" fill="none" stroke="#fff" stroke-width="1.5"/></svg></span>
      <span class="on"><svg width="8" height="8" viewBox="0 0 8 8"><path d="M2.5 1l3 3-3 3" fill="none" stroke="#fff" stroke-width="1.5"/></svg></span>
    </div>
  </div>
  <div class="tiles">
    <div class="tile tile-stats" role="img" aria-label="Rising golden arrow over blue bar chart"><h3>Statistical Productivity Improvement</h3><p>The flagship service provided by VPG</p></div>
    <div class="tile tile-project" role="img" aria-label="Stack of paper project documents"><h3>Improving Project Performance</h3><p>A structured review for project management to find root causes and correct issues.</p></div>
    <div class="tile tile-training" role="img" aria-label="Team gathered around a laptop in a training session"><h3>On-Site Training</h3><p>We evaluate training needs, assess resources and provide hands-on training solutions.</p></div>
    <div class="tile tile-veradin" role="img" aria-label="Pen resting on a printed document"><h3>Veradin Process</h3><p>Provides great insight to management about how crew time is utilized.</p></div>
    <div class="tile tile-mapping" role="img" aria-label="Hand holding a tablet with a process chart"><h3>Work Process Analysis &amp; Mapping</h3><p>Maps core work processes to identify constraints directly affecting construction.</p></div>
    <div class="tile tile-facilitation" role="img" aria-label="Hand holding a glowing globe"><h3>Facilitation</h3><p>Focus on directing project human resources to plan, implement, &amp; drive performance improvement initiatives.</p></div>
  </div>
</section>

<section class="block join">
  <p class="join-text">JOIN US : Apply today to become a member of the VPG family.</p>
  <div class="join-btn">EXPLORE CAREER OPPORTUNITIES</div>
</section>

<section class="block updates">
  <div class="news">
    <h2 class="title-line">Latest <strong>News</strong></h2>
    <div class="news-item"><h4>VPG delivering keynote speech for the 2015 FEX Conference</h4><p>Integer facilisis pharetra risus eget auctor. Nullam viverra dapibus tellus, sit amet cursus turpis vulputate consectetur.</p></div>
    <div class="news-item"><h4>Phasellus commodo lorem elit nulla</h4><p>Integer facilisis pharetra risus eget auctor. Nullam viverra dapibus tellus, sit amet cursus turpis vulputate consectetur.</p></div>
    <div class="news-item"><h4>Duis viverra ultricies nisi ut fermentum</h4><p>Integer facilisis pharetra risus eget auctor. Nullam viverra dapibus tellus, sit amet cursus turpis vulputate consectetur.</p></div>
  </div>
  <div class="testimonials">
    <h2 class="title-line">Clients <strong>Testimonials</strong></h2>
    <div class="quote"><div class="avatar" role="img" aria-label="Portrait photo of a client in a suit"></div><p>Praesent dignissim sem sapien, a vulputate enim auctor vitae. Duis non lorem porta, adipiscing eros sit amet, tempor sem.<br><em>- Lena Fairbrook</em></p></div>
    <div class="quote"><div class="avatar" role="img" aria-label="Portrait photo of a smiling client"></div><p>Nunc at pretium est curabitur commodo leac est venenatis egestas sed aliquet auguevelit - <em>Nora Dennick</em></p></div>
  </div>
</section>

<footer class="block footer">
  <div class="foot-logo"><span class="brand-mark"></span><span class="brand-name">Veltrane Performance Group</span></div>
  <div class="foot-contact">
    <div><svg width="8" height="11" viewBox="0 0 8 11"><path d="M4 0a4 4 0 0 1 4 4c0 3-4 7-4 7S0 7 0 4a4 4 0 0 1 4-4z" fill="#9a9a9a"/><circle cx="4" cy="4" r="1.5" fill="#2f2f2f"/></svg>P.O. Box 218, Larkfield, NC 20418</div>
    <div><svg width="9" height="10" viewBox="0 0 9 10"><path d="M1 1h2l1 2.5-1.2.8a5 5 0 0 0 2.9 2.9L6.5 6 9 7v2a1 1 0 0 1-1 1A8 8 0 0 1 0 2a1 1 0 0 1 1-1z" fill="#9a9a9a"/></svg>+1 555.014.2289</div>
    <div><svg width="11" height="8" viewBox="0 0 11 8"><rect width="11" height="8" fill="#9a9a9a"/><path d="M0 0 5.5 4.5 11 0" fill="none" stroke="#2f2f2f"/></svg>contact@veltraneperf.com</div>
  </div>
  <div class="foot-map" role="img" aria-label="Faint world map decoration"></div>

  <div class="foot-col" style="left:387px">
    <h5>Useful <strong>Links</strong></h5>
    <ul><li>Home</li><li>Services</li><li>News &amp; Insights</li><li>About Us</li><li>Contact</li><li>Career</li><li>Login</li></ul>
  </div>
  <div class="foot-col" style="left:618px">
    <h5>Useful <strong>Links</strong></h5>
    <ul><li>Statistical Productivity<br>Improvement</li><li>Veradin Process</li><li>Improving Project Performance</li><li>Work Process Analysis &amp; Mapping</li><li>On-Site Training</li><li>Facilitation</li></ul>
  </div>
  <div class="foot-col" style="left:849px;width:195px">
    <h5>Latest <strong>Tweets</strong></h5>
    <div class="tweet"><span class="tweet-dot"></span><div>loomstudio7: hostrelay - Responsive html5 Professional Hosting Theme<small>2 days ago · reply · retweet · favorite</small></div></div>
    <div class="tweet" style="border:0"><span class="tweet-dot"></span><div>loomstudio7: Corvexa - Responsive HTML5 / CSS3, Professional Corporate Theme.<small>3 days ago · reply · retweet · favorite</small></div></div>
  </div>
</footer>

<div class="block bottom">
  <div class="notch"></div>
  <p class="copyright">Copyright © 2015 Veltrane Performance Group, Inc. (VPG) . All rights reserved. Terms of Use | Privacy Policy</p>
  <div class="bottom-social"><span></span><span></span><span></span><span></span><span></span><span></span><span></span></div>
</div>

</body>
</html>
```